Byaruhanga & Odongo Advocates website

An interactive professional law firm website fully synchronized with social media pages.

Target Market(s)

Corporations and professionals

Industry/Entity Type

Professional Service

Number of Pages Required

5+ page

Font styles to use
Sans Serif

Colors

Designer to choose colors to be used in the design.

```html
<!DOCTYPE html>
<html lang="en">
<head>
<meta charset="utf-8">
<title>Byaruhanga &amp; Odongo Advocates</title>
<link href="https://fonts.googleapis.com/css2?family=Open+Sans:wght@400;600;700&family=Source+Sans+3:wght@400;600;700&display=swap" rel="stylesheet">
<style>
:root{
  --red:#8e1b26;
  --red-deep:#5f1219;
  --red-dark:#4a0e14;
  --ink:#2b2b2b;
  --text:#6f6f6f;
  --muted:#9a9a9a;
  --line:#e3e3e6;
  --paper:#ffffff;
  --mist:#f1f2f6;
  --night:#1f1f22;
}
*{margin:0;padding:0;box-sizing:border-box}
html,body{width:1200px;height:3876px;overflow:hidden}
body{font-family:"Open Sans",Arial,sans-serif;color:var(--text);background:var(--paper);position:relative}
.section{position:absolute;left:0;width:1200px}
h2,h3,h4{font-family:"Source Sans 3","Open Sans",sans-serif;color:var(--ink);letter-spacing:1px}

/* header */
.site-header{top:0;height:68px;background:var(--paper);box-shadow:0 1px 4px rgba(0,0,0,.08);z-index:3}
.brand{position:absolute;left:232px;top:22px;display:flex;align-items:center;gap:10px}
.brand-square{width:22px;height:22px;background:var(--red)}
.brand-name{font-size:12px;line-height:15px;color:var(--ink);font-weight:600;width:170px}
.main-nav{position:absolute;left:510px;top:26px;display:flex;gap:38px;font-size:11px;font-weight:600;color:var(--ink)}
.main-nav .active{color:var(--red);border-bottom:2px solid var(--red);padding-bottom:6px}

/* hero */
.hero{top:68px;height:600px}
.hero-photo{position:absolute;inset:0;background:radial-gradient(circle at 30% 40%,#7a4a2a 0%,#3d2416 35%,#1c120d 70%);}
.hero-text{position:absolute;top:126px;width:100%;text-align:center;color:#fff}
.hero-kicker{font-size:16px;color:#f0d9b8}
.hero-title{font-family:"Source Sans 3",sans-serif;font-size:44px;font-weight:700;letter-spacing:3px;margin-top:6px;color:#fff}
.btn{display:inline-block;font-size:11px;font-weight:700;letter-spacing:1px;color:#fff;background:var(--red);padding:10px 24px}
.hero .btn{margin-top:44px}
.slide-arrow{position:absolute;top:200px;width:26px;height:26px;background:rgba(255,255,255,.2);}
.slide-arrow.left{left:30px}.slide-arrow.right{right:30px;background:var(--red)}
.hero-wave{position:absolute;bottom:0;left:0}
.hero-badge{position:absolute;left:586px;top:530px;width:28px;height:28px;border-radius:50%;background:var(--red);border:3px solid #fff}

/* history */
.history{top:690px;height:340px}
.history-photo{position:absolute;left:232px;top:22px;width:328px;height:288px;background:linear-gradient(135deg,#d9b79a,#8a5a3c 60%,#f3e6d8)}
.history-body{position:absolute;left:600px;top:28px;width:370px}
.section-title{font-size:20px;font-weight:700;border-left:3px solid var(--red);padding-left:10px}
.history-body p{margin-top:18px;font-size:11.5px;line-height:19px}

/* practice areas */
.practice{top:1060px;height:340px;border-top:1px solid var(--line)}
.center-title{text-align:center;font-size:22px;font-weight:700}
.practice .center-title{margin-top:52px}
.practice-grid{position:absolute;top:124px;left:220px;display:flex;gap:40px}
.practice-item{width:240px;text-align:center}
.practice-item h3{font-size:13px;color:var(--red);font-weight:700;margin-top:14px}
.practice-item p{font-size:10.5px;line-height:17px;margin-top:10px}

/* who we are */
.who{top:1428px;height:484px}
.who-panel{position:absolute;left:0;top:0;width:652px;height:484px;background:var(--red)}
.who-photo{position:absolute;left:652px;top:0;width:548px;height:484px;background:linear-gradient(160deg,#3a3a44,#1a1a22 55%,#50505a)}
.who-panel .edge{position:absolute;left:28px;top:224px;width:3px;height:26px;background:#fff}
.who-panel h2{position:absolute;right:52px;top:92px;color:#fff;font-size:22px;font-weight:700}
.who-panel h2::after{content:"";display:block;width:40px;height:2px;background:#fff;margin:8px 0 0 auto}
.who-lead{position:absolute;right:52px;top:140px;width:400px;color:#f3dcdf;font-size:11px;line-height:18px;text-align:right}
.who-point{position:absolute;right:76px;width:380px;text-align:right;color:#f3dcdf;font-size:11px;line-height:18px}
.who-point h4{color:#fff;font-size:12px;font-weight:700}
.who-icon{position:absolute;right:-44px;top:4px;width:32px;height:32px;border-radius:50%;background:#fff;display:flex;align-items:center;justify-content:center}

/* clients */
.clients{top:1912px;height:528px;background:var(--mist)}
.clients .center-title{margin-top:88px}
.clients .sub{text-align:center;font-size:11px;margin-top:10px}
.client-grid{position:absolute;left:232px;top:208px;display:grid;grid-template-columns:repeat(6,124px);gap:16px 14px}
.client{height:64px;background:#fff;display:flex;align-items:center;justify-content:center;gap:6px;font-family:"Source Sans 3",sans-serif;font-size:12px;font-weight:600;color:var(--muted)}
.client.hl{background:#e2504a;color:#fff}
.client i{width:10px;height:10px;background:currentColor;border-radius:50%}
.btn-outline{display:block;width:152px;margin:0 auto;border:1px solid #b8b8be;text-align:center;font-size:10px;font-weight:700;color:var(--ink);padding:9px 0;letter-spacing:1px}
.clients .btn-outline{position:absolute;left:524px;top:418px}

/* stats */
.stats{top:2440px;height:320px}
.stats-photo{position:absolute;inset:0;background:linear-gradient(180deg,#2c2426,#171415 60%,#2a2020)}
.stat-row{position:absolute;top:86px;left:230px;display:flex;gap:88px}
.stat{width:110px;text-align:center;color:#fff}
.stat-icon{width:44px;height:44px;border:2px solid rgba(255,255,255,.6);border-radius:50%;margin:0 auto;display:flex;align-items:center;justify-content:center}
.stat strong{display:block;font-size:22px;margin-top:64px;font-family:"Source Sans 3",sans-serif}
.stat span{font-size:10px;color:#cfcfcf}

/* team */
.team{top:2760px;height:420px;background:#fafafa}
.team .center-title{margin-top:44px}
.team-grid{position:absolute;left:296px;top:104px;display:flex;gap:16px}
.member{width:138px;text-align:center}
.member-photo{height:140px;background:linear-gradient(180deg,#6c6c74,#2a2a30)}
.member h4{font-size:10px;margin-top:18px;font-weight:700}
.member p{font-size:9px;color:var(--muted)}
.team .btn-outline{position:absolute;left:534px;top:338px;width:132px}

/* contact */
.contact{top:3180px;height:640px;background:linear-gradient(180deg,var(--red-deep),var(--red-dark))}
.contact h2{color:#fff;text-align:center;font-size:20px;margin-top:36px;font-weight:700}
.contact .sub{text-align:center;color:#e2c3c6;font-size:11px;margin-top:8px}
.card{position:absolute;top:188px;background:#fff;height:352px}
.card.address{left:232px;width:296px;padding:46px 28px;font-size:11px;line-height:17px}
.card.address h4{color:var(--red);font-size:12px;font-weight:700;margin-top:18px}
.card.address h4:first-child{margin-top:0}
.card.form{left:544px;width:424px;padding:40px 30px}
.field{border-bottom:1px solid var(--line);font-size:11px;color:var(--muted);padding:10px 0;margin-bottom:10px}
.field.msg{height:120px}
.card.form .btn{margin-top:10px}

/* footer */
.site-footer{top:3820px;height:56px;background:var(--night)}
.social{position:absolute;left:256px;top:22px;display:flex;gap:12px}
.social i{width:12px;height:12px;border-radius:50%;background:#8b8b90}
.copyright{position:absolute;right:232px;top:20px;font-size:10px;color:#8b8b90}
.to-top{position:absolute;right:36px;top:14px;width:28px;height:28px;border-radius:50%;background:var(--red)}
</style>
</head>
<body>

<header class="section site-header">
  <div class="brand"><span class="brand-square"></span><span class="brand-name">Byaruhanga &amp; Odongo Advocates</span></div>
  <nav class="main-nav"><span class="active">HOME</span><span>ABOUT US</span><span>WHO WE ARE</span><span>CLIENTS</span><span>TEAM</span><span>BLOG</span><span>CONTACT</span></nav>
</header>

<section class="section hero">
  <div class="hero-photo" role="img" aria-label="Wooden gavel, scales of justice and law books on a dark desk"></div>
  <span class="slide-arrow left"></span><span class="slide-arrow right"></span>
  <div class="hero-text">
    <p class="hero-kicker">Our Clients Are Our First Priority</p>
    <h1 class="hero-title">WELCOME TO B&amp;O</h1>
    <a class="btn">OUR EXPERTISE</a>
  </div>
  <svg class="hero-wave" width="1200" height="110" viewBox="0 0 1200 110"><path d="M0 40 Q600 150 1200 30 L1200 110 L0 110 Z" fill="#fff"/></svg>
  <span class="hero-badge"></span>
</section>

<section class="section history">
  <div class="history-photo" role="img" aria-label="Bronze scales of justice on a desk"></div>
  <div class="history-body">
    <h2 class="section-title">OUR HISTORY</h2>
    <p>Byaruhanga &amp; Odongo Advocates was founded by two partners who shared one goal: to give companies and professionals clear, reliable legal advice. From a small office with three staff, the firm has grown into a full practice serving clients across the region and beyond.</p>
    <p>Over the years we have advised on major building projects, complex commercial disputes and cross-border arbitration. Our lawyers combine deep local knowledge with sound international practice, and every matter is led by a partner who knows the client well.</p>
    <p>Today the firm remains guided by the same values of integrity, diligence and care that shaped its first case, and we continue to build lasting partnerships with the people we serve.</p>
  </div>
</section>

<section class="section practice">
  <h2 class="center-title">PRACTICE AREAS</h2>
  <div class="practice-grid">
    <div class="practice-item">
      <svg width="40" height="40" viewBox="0 0 40 40"><rect x="8" y="8" width="24" height="24" transform="rotate(45 20 20)" fill="none" stroke="#8e1b26" stroke-width="2"/><path d="M14 24 L20 14 L26 24 Z" fill="#8e1b26"/></svg>
      <h3>CONSTRUCTION LAW</h3>
      <p>We advise developers, contractors and owners on contracts, tenders, claims and disputes at every stage of a building project.</p>
    </div>
    <div class="practice-item">
      <svg width="40" height="40" viewBox="0 0 40 40"><rect x="8" y="8" width="24" height="24" transform="rotate(45 20 20)" fill="none" stroke="#8e1b26" stroke-width="2"/><rect x="13" y="18" width="14" height="4" fill="#8e1b26" transform="rotate(-35 20 20)"/></svg>
      <h3>COMMERCIAL / LITIGATION</h3>
      <p>Our litigators represent companies in commercial courts, protecting their interests in contract, banking and shareholder disputes.</p>
    </div>
    <div class="practice-item">
      <svg width="40" height="40" viewBox="0 0 40 40"><rect x="8" y="8" width="24" height="24" transform="rotate(45 20 20)" fill="none" stroke="#8e1b26" stroke-width="2"/><path d="M12 20 H28 M20 13 V27" stroke="#8e1b26" stroke-width="2"/></svg>
      <h3>ARBITRATION</h3>
      <p>We guide clients through local and international arbitration, from drafting clauses to presenting cases before the tribunal.</p>
    </div>
  </div>
</section>

<section class="section who">
  <div class="who-panel">
    <span class="edge"></span>
    <h2>WHO WE ARE</h2>
    <p class="who-lead">We are a team of advocates, consultants and support staff committed to practical, timely legal solutions. Our people bring decades of combined experience in business law and dispute resolution, and we work as one team for every client.</p>
    <div class="who-point" style="top:270px"><span class="who-icon"><svg width="16" height="16" viewBox="0 0 16 16"><path d="M1 8 Q8 1 15 8 Q8 15 1 8 Z" fill="none" stroke="#8e1b26" stroke-width="1.5"/><circle cx="8" cy="8" r="2.5" fill="#8e1b26"/></svg></span><h4>VISION</h4><p>To be the most trusted business law firm in the region.</p></div>
    <div class="who-point" style="top:362px"><span class="who-icon"><svg width="16" height="16" viewBox="0 0 16 16"><circle cx="8" cy="8" r="6.5" fill="none" stroke="#8e1b26" stroke-width="1.5"/><circle cx="8" cy="8" r="3" fill="none" stroke="#8e1b26" stroke-width="1.5"/><circle cx="8" cy="8" r="1" fill="#8e1b26"/></svg></span><h4>MISSION</h4><p>To deliver sound, honest and efficient legal services that help our clients grow with confidence.</p></div>
  </div>
  <div class="who-photo" role="img" aria-label="Group portrait of the firm's lawyers in business suits"></div>
</section>

<section class="section clients">
  <h2 class="center-title">OUR CLIENTS</h2>
  <p class="sub">We are proud to work with leading companies and institutions across many sectors.</p>
  <div class="client-grid">
    <div class="client"><i></i>Sunmark</div>
    <div class="client">Orvel Foods</div>
    <div class="client">Halden Group</div>
    <div class="client"><i></i>Tessara</div>
    <div class="client">Lumio Bank</div>
    <div class="client"><i></i>Kestra</div>
    <div class="client">Nordane</div>
    <div class="client hl">Pelmor</div>
    <div class="client">Vantry Co</div>
    <div class="client"><i></i>Ardent</div>
    <div class="client">Brisk Energy</div>
    <div class="client">Calvex</div>
  </div>
  <a class="btn-outline">VIEW MORE</a>
</section>

<section class="section stats">
  <div class="stats-photo" role="img" aria-label="Busy city street with people walking, darkened"></div>
  <div class="stat-row">
    <div class="stat"><div class="stat-icon"><svg width="22" height="22" viewBox="0 0 22 22" fill="#fff"><circle cx="7" cy="7" r="3"/><circle cx="15" cy="7" r="3"/><path d="M1 19 Q1 12 7 12 Q13 12 13 19 Z"/><path d="M9 19 Q9 12 15 12 Q21 12 21 19 Z"/></svg></div><strong>7</strong><span>Partners</span></div>
    <div class="stat"><div class="stat-icon"><svg width="22" height="22" viewBox="0 0 22 22" fill="none" stroke="#fff" stroke-width="1.8"><rect x="2" y="7" width="18" height="12" rx="1"/><path d="M8 7 V4 H14 V7 M2 12 H20"/></svg></div><strong>20+</strong><span>Lawyers</span></div>
    <div class="stat"><div class="stat-icon"><svg width="22" height="22" viewBox="0 0 22 22" fill="none" stroke="#fff" stroke-width="1.8"><rect x="2" y="4" width="18" height="16" rx="1"/><path d="M2 9 H20 M7 2 V6 M15 2 V6"/><rect x="6" y="12" width="3" height="3" fill="#fff" stroke="none"/></svg></div><strong>25+</strong><span>Years of Practice</span></div>
    <div class="stat"><div class="stat-icon"><svg width="22" height="22" viewBox="0 0 22 22" fill="#fff"><rect x="2" y="14" width="4" height="6"/><rect x="8" y="10" width="4" height="10"/><rect x="14" y="5" width="4" height="15"/><path d="M2 10 L9 5 L13 7 L20 2" fill="none" stroke="#fff" stroke-width="1.5"/></svg></div><strong>350+</strong><span>Cases Closed</span></div>
  </div>
</section>

<section class="section team">
  <h2 class="center-title">MEET OUR PROFESSIONALS</h2>
  <div class="team-grid">
    <div class="member"><div class="member-photo" role="img" aria-label="Portrait of a partner"></div><h4>PAUL K. NSUBUGA</h4><p>Managing Partner</p></div>
    <div class="member"><div class="member-photo" role="img" aria-label="Portrait of a partner"></div><h4>DAVID A. OKELLO</h4><p>Senior Partner</p></div>
    <div class="member"><div class="member-photo" role="img" aria-label="Portrait of an associate"></div><h4>JOHN MUKASA</h4><p>Associate</p></div>
    <div class="member"><div class="member-photo" role="img" aria-label="Portrait of an associate"></div><h4>PETER WAISWA</h4><p>Associate</p></div>
  </div>
  <a class="btn-outline">VIEW ALL</a>
</section>

<section class="section contact">
  <h2>KEEP IN TOUCH</h2>
  <p class="sub">We would love to hear from you. Send us a message and we will reply soon.</p>
  <div class="card address">
    <h4>OUR ADDRESS</h4>
    <p>Plot 14 Meridian Road<br>Third Floor, Crest House<br>P.O. Box 4521<br>Kampala, Uganda</p>
    <h4>CALL US</h4>
    <p>Telephone: +256 700 000 111<br>Mobile: +256 700 000 222</p>
    <h4>EMAIL US</h4>
    <p>info@byaruhanga-odongo.example</p>
  </div>
  <div class="card form">
    <div class="field">Name</div>
    <div class="field">Email</div>
    <div class="field">Subject</div>
    <div class="field msg">Message</div>
    <a class="btn">SEND MESSAGE</a>
  </div>
</section>

<footer class="section site-footer">
  <div class="social"><i></i><i></i><i></i><i></i><i></i></div>
  <p class="copyright">© 2024 Byaruhanga &amp; Odongo Advocates. All rights reserved.</p>
  <span class="to-top"></span>
</footer>

</body>
</html>
```